Design for company homepage promoting to the pharmaceutical industry

Our company produces medical education materials and services for the pharmaceutical industry. Our existing website (www.quorvan.net.au) provides more information.
 
We need a homepage design for our new company website we are creating. Our site will not have a great amount of content, we want it to be fast, user friendly and easily adaptable to viewing on any platform, and through any browser. We don't want it over-designed - i.e. no highly animated banner flags, backgrounds, obscure webfonts, too many graphics etc. Attached are files indicating our existing company logo and design. We want the logo and rings to be retained. We've also attached draft copy for the website.
The final website may be designed in Wordpress (still to be confirmed)
 
This is a design to replace the current site (www.quorvan.net.au). Content will also be revised.
Things we don't like about our current design - doesn't use our current branding, is not very exciting, old fashioned 'standard' format, too much content, just doesn't look that good, boring.
 
Examples of sites we like:
www.brelmot.com.au
http://factsheets.wondipaq.com.au/index.html
 
Features we like from these sites - fast, responsive, short and to the point, cross-platform compatible including smartphones, and looks good
 
Main reasons people will visit our site: to find out whether we can provide services they might be looking for, to make a decision on whether they are interested in what we offer so they can get in touch with us, and to get our contact details.
Main thing we want to achieve from website visits is that it looks good enough and provides enough summary information on us so that they want to get in touch with us, to offer us work or to ask us to come in and meet them to provide more info on what we do.
Two most important calls to action from our website
· make the decision that we can do what you are looking for
· get in touch with us.
Updates

Thanks everyone for your submissions. At this stage with the Christmas break upon us, we are yet to finalise our decision, and will make a decision early in the new year. I hope everyone has a good holiday break.
Kind regards
Doug

Target Market(s)

Pharmaceutical industry professionals, marketers and medical professionals.

Industry/Entity Type

Pharmaceutical

Requirements
Must have
• Company logo and rings must be incorporated, company colour - blue - must be in there.
Should not have
• Complex animation or graphics that will slow the upload or limit cross-platform compatability/viewing on smartphones etc.

```html
<!DOCTYPE html>
<html lang="en">
<head>
<meta charset="utf-8">
<title>Quorvan Healthcare Education</title>
<link href="https://fonts.googleapis.com/css2?family=Ubuntu:wght@300;400;500&family=Open+Sans:wght@400;600&display=swap" rel="stylesheet">
<style>
:root{
  --blue:#1c5a92;
  --blue-dark:#164a79;
  --blue-light:#6f9fcc;
  --charcoal:#2c2c2c;
  --footer:#262626;
  --grey-bg:#eeeeee;
  --rule:#d6d6d6;
  --text:#4a4a4a;
  --muted:#8a8a8a;
  --white:#ffffff;
}
*{margin:0;padding:0;box-sizing:border-box}
html,body{width:1200px;height:3220px;overflow:hidden}
body{font-family:"Open Sans",Arial,sans-serif;color:var(--text);background:var(--white);font-size:15px}
.wrap{width:940px;margin:0 auto;position:relative}
h2.section-title{font-family:"Ubuntu",sans-serif;font-weight:300;font-size:52px;color:var(--blue-dark);text-align:center;letter-spacing:1px}

/* header */
.site-header{height:144px;background:var(--white)}
.site-header .wrap{height:144px;display:flex;align-items:center;justify-content:space-between}
.brand{display:flex;align-items:center;gap:14px;text-decoration:none}
.brand-dot{width:22px;height:22px;border-radius:50%;background:var(--blue)}
.brand-name{font-family:"Ubuntu",sans-serif;font-weight:300;font-size:60px;color:var(--blue)}
.search{width:280px;height:30px;border:1px solid var(--rule);display:flex;align-items:center;justify-content:flex-end;padding-right:8px}

/* nav */
.main-nav{height:48px;background:var(--blue)}
.main-nav ul{list-style:none;display:flex;height:48px;width:940px;margin:0 auto}
.main-nav li{font-family:"Ubuntu",sans-serif;font-size:17px;color:var(--white);padding:0 24px;line-height:48px}
.main-nav li.active{background:#c9d9e8;color:var(--blue-dark)}

/* hero */
.hero{height:400px;background:var(--charcoal);color:#e8e8e8;padding-top:40px}
.hero h1{font-family:"Ubuntu",sans-serif;font-weight:400;font-size:31px;text-align:center;color:var(--white);line-height:40px}
.hero p{width:860px;margin:28px auto 14px;font-size:14px;line-height:21px;color:#cfcfcf}
.hero ul{list-style:none;width:860px;margin:0 auto}
.hero li{font-size:14px;line-height:21px;margin-bottom:10px;padding-left:28px;position:relative;color:#dcdcdc}
.hero li svg{position:absolute;left:0;top:3px}

/* who we are */
.who{height:358px;padding-top:20px;text-align:center}
.who .tagline{font-family:"Ubuntu",sans-serif;font-weight:300;font-size:20px;color:var(--muted);margin-top:4px}
.portrait{width:96px;height:96px;border-radius:50%;margin:24px auto 10px;background:linear-gradient(#c9d3de,#8d9cb0);border:4px solid #dde6ef}
.person{font-family:"Ubuntu",sans-serif;font-size:16px;color:var(--blue);font-weight:500}
.who p{width:900px;margin:14px auto 0;text-align:left;font-size:14px;line-height:21px}

/* what we do */
.services{height:370px;background:var(--grey-bg);padding-top:38px}
.service-list{display:flex;justify-content:center;gap:56px;margin-top:28px}
.service{width:126px;text-align:center}
.service .icon{width:104px;height:104px;border-radius:50%;background:#dde3ea;margin:0 auto;display:flex;align-items:center;justify-content:center}
.service h3{font-family:"Ubuntu",sans-serif;font-weight:400;font-size:27px;color:var(--blue-dark);margin:14px 0 12px}
.btn{display:inline-block;background:var(--blue);color:var(--white);font-size:13px;font-weight:600;padding:0 22px;line-height:30px;border-radius:3px}

/* work */
.work{height:580px;padding-top:60px;text-align:center}
.gallery{display:flex;justify-content:center;gap:36px;margin-top:46px;height:350px}
.shot{width:210px;height:350px}
.shot.wide{width:290px}
.work .btn{font-size:17px;padding:0 44px;line-height:52px;margin-top:32px;font-family:"Ubuntu",sans-serif;font-weight:400}

/* testimonials */
.testimonials{height:340px;background:var(--grey-bg);padding-top:40px}
.testimonials .head{display:flex;align-items:center;justify-content:center;gap:22px}
.testimonials .head h2{font-size:44px}
.quotes{display:flex;gap:40px;width:940px;margin:36px auto 0}
.quote{flex:1;display:flex;gap:14px}
.quote .mark{font-family:Georgia,serif;font-size:56px;line-height:44px;color:var(--blue-light)}
.quote p{font-size:14px;line-height:21px;font-style:italic;color:#555}
.dots{display:flex;justify-content:center;gap:10px;margin-top:32px}
.dots span{width:12px;height:12px;border-radius:50%;background:#9fb3c7}
.dots span.on{background:var(--blue)}

/* clients */
.clients{height:280px;padding-top:30px}
.client-grid{display:grid;grid-template-columns:repeat(4,200px);justify-content:center;gap:26px 30px;margin-top:32px}
.client{display:flex;align-items:center;justify-content:center;gap:8px;font-family:"Open Sans",sans-serif;font-weight:600;font-size:19px;color:var(--blue-dark);height:50px}
.client i{width:12px;height:12px;background:var(--blue-light);display:block}

/* get in touch */
.touch{height:130px;background:var(--blue);display:flex;align-items:center}
.touch h2{font-family:"Ubuntu",sans-serif;font-weight:400;font-size:54px;color:var(--white);width:1060px;margin:0 auto}

/* footer */
.site-footer{height:220px;background:var(--footer);color:#d0d0d0;font-size:14px;line-height:22px}
.footer-main{width:940px;margin:0 auto;padding-top:36px;display:flex;gap:90px;height:176px}
.footer-main dl{display:grid;grid-template-columns:90px auto;column-gap:10px}
.footer-main dt{color:#9a9a9a}
.social{display:flex;gap:10px;margin-left:auto}
.social span{width:30px;height:30px;border-radius:50%;background:var(--blue-light)}
.copyright{border-top:1px solid #3a3a3a;width:1060px;margin:0 auto;padding-top:10px;font-size:12px;color:#9a9a9a}
.copyright b{color:var(--blue-light);font-weight:400}

/* map */
.map{height:350px;background:linear-gradient(160deg,#e4e8d8 0%,#d8dccb 45%,#b9cfe2 60%,#e4e6dc 100%)}
</style>
</head>
<body>

<header class="site-header">
  <div class="wrap">
    <a class="brand"><span class="brand-dot"></span><span class="brand-name">quorvan</span></a>
    <div class="search">
      <svg width="16" height="16" viewBox="0 0 16 16"><circle cx="6.5" cy="6.5" r="5" fill="none" stroke="#999" stroke-width="1.6"/><line x1="10.5" y1="10.5" x2="15" y2="15" stroke="#999" stroke-width="1.6"/></svg>
    </div>
  </div>
</header>

<nav class="main-nav">
  <ul>
    <li class="active">home</li><li>who we are</li><li>what we do</li><li>some of our work</li><li>who we work with</li><li>contact us</li>
  </ul>
</nav>

<section class="hero">
  <h1>At Quorvan we are healthcare communication specialists;<br>this means we're scientists, journalists and marketers rolled into one.</h1>
  <p>As you can see we can provide all the things you'd expect from a top class healthcare communications agency, but we have the depth of technical understanding and creative flair to produce sophisticated and memorable materials and programs, including:</p>
  <ul>
    <li><svg width="14" height="14" viewBox="0 0 14 14"><path d="M1 7l4 4 8-9" fill="none" stroke="#6f9fcc" stroke-width="2"/></svg>Strategic tools for brand promotion (such as detail aids, product monographs, slide kits and patient materials)</li>
    <li><svg width="14" height="14" viewBox="0 0 14 14"><path d="M1 7l4 4 8-9" fill="none" stroke="#6f9fcc" stroke-width="2"/></svg>Non-promotional materials for market education (e.g. clinical papers and evidence summaries)</li>
    <li><svg width="14" height="14" viewBox="0 0 14 14"><path d="M1 7l4 4 8-9" fill="none" stroke="#6f9fcc" stroke-width="2"/></svg>Complete programs such as clinical audits and product familiarisation programs</li>
    <li><svg width="14" height="14" viewBox="0 0 14 14"><path d="M1 7l4 4 8-9" fill="none" stroke="#6f9fcc" stroke-width="2"/></svg>Medical meetings and symposia</li>
  </ul>
</section>

<section class="who">
  <h2 class="section-title">who we are</h2>
  <div class="tagline">we are proud of what we do.</div>
  <div class="portrait" role="img" aria-label="Portrait photo of the managing director"></div>
  <div class="person">Doug Harrow Managing Director</div>
  <p>After graduating with honours from Ashdale University, UK, Doug entered the pharmaceutical industry as an information scientist. He soon moved into medical education and entered the competitive European healthcare communications marketplace. He worked for a number of healthcare education agencies in the UK before moving to Australia and setting up Quorvan in 2000.</p>
</section>

<section class="services">
  <h2 class="section-title">what we do</h2>
  <div class="service-list">
    <div class="service">
      <div class="icon"><svg width="54" height="44" viewBox="0 0 54 44"><path d="M2 6l16-4 18 4 16-4v36l-16 4-18-4-16 4z" fill="#7fa6cc"/><path d="M18 2v36M36 6v36" stroke="#fff" stroke-width="2"/></svg></div>
      <h3>promotion</h3><span class="btn">Learn More</span>
    </div>
    <div class="service">
      <div class="icon"><svg width="40" height="50" viewBox="0 0 40 50"><circle cx="20" cy="12" r="10" fill="#7fa6cc"/><path d="M2 50c0-14 8-24 18-24s18 10 18 24z" fill="#7fa6cc"/></svg></div>
      <h3>education</h3><span class="btn">Learn More</span>
    </div>
    <div class="service">
      <div class="icon"><svg width="54" height="48" viewBox="0 0 54 48"><rect x="2" y="2" width="50" height="32" fill="#7fa6cc"/><rect x="8" y="8" width="38" height="20" fill="#fff"/><path d="M27 34v10M16 46l11-10 11 10" stroke="#7fa6cc" stroke-width="3" fill="none"/></svg></div>
      <h3>programs</h3><span class="btn">Learn More</span>
    </div>
    <div class="service">
      <div class="icon"><svg width="58" height="44" viewBox="0 0 58 44"><circle cx="14" cy="12" r="7" fill="#7fa6cc"/><circle cx="44" cy="12" r="7" fill="#7fa6cc"/><path d="M2 40c0-10 5-18 12-18s12 8 12 18zM32 40c0-10 5-18 12-18s12 8 12 18z" fill="#7fa6cc"/></svg></div>
      <h3>meetings</h3><span class="btn">Learn More</span>
    </div>
    <div class="service">
      <div class="icon"><svg width="52" height="44" viewBox="0 0 52 44"><rect x="2" y="8" width="48" height="34" rx="4" fill="#7fa6cc"/><rect x="18" y="2" width="16" height="8" fill="none" stroke="#7fa6cc" stroke-width="3"/><path d="M26 16v18M17 25h18" stroke="#fff" stroke-width="5"/></svg></div>
      <h3>IME</h3><span class="btn">Learn More</span>
    </div>
  </div>
</section>

<section class="work">
  <h2 class="section-title">some of our work</h2>
  <div class="gallery">
    <div class="shot" role="img" aria-label="Photo of printed brochures fanned out" style="background:linear-gradient(135deg,#e8eef3,#7aa6c8 55%,#f1c36a)"></div>
    <div class="shot" role="img" aria-label="Photo of a blue product folder and booklets" style="background:linear-gradient(160deg,#f2f4f6,#3d7fb6 60%,#dfe6ec)"></div>
    <div class="shot wide" role="img" aria-label="Photo of stacked publications and slide kits" style="background:linear-gradient(145deg,#f6f3ea,#e6c9a4 45%,#c44b4b 80%,#f0f0f0)"></div>
  </div>
  <span class="btn">view our gallery</span>
</section>

<section class="testimonials">
  <div class="head">
    <svg width="64" height="54" viewBox="0 0 64 54"><ellipse cx="30" cy="24" rx="28" ry="21" fill="var(--blue)"/><path d="M14 38l-6 14 18-10z" fill="var(--blue)"/><circle cx="20" cy="24" r="3" fill="#fff"/><circle cx="30" cy="24" r="3" fill="#fff"/><circle cx="40" cy="24" r="3" fill="#fff"/></svg>
    <h2 class="section-title">what our clients are saying</h2>
  </div>
  <div class="quotes">
    <div class="quote"><span class="mark">“</span><p>Congratulations &amp; many thanks for your seriously wonderful &amp; successful work on the weekend. I'm especially grateful for the calm, cool &amp; very clever work done in managing all the planning process before I even came on board – truly outstanding</p></div>
    <div class="quote"><span class="mark">“</span><p>I wanted to thank you for your work – I know you came thrown into the deep end with this meeting and also our sometimes unrealistic expectations – you did a fantastic job! All the team know what a great job Quorvan do on these meetings</p></div>
  </div>
  <div class="dots"><span class="on"></span><span></span><span></span></div>
</section>

<section class="clients">
  <h2 class="section-title">some of our clients</h2>
  <div class="client-grid">
    <div class="client"><i></i>Velmora</div>
    <div class="client"><i></i>Ostrin</div>
    <div class="client"><i></i>Kandel</div>
    <div class="client"><i></i>Threlby</div>
    <div class="client"><i></i>Marwen</div>
    <div class="client"><i></i>Corvalis</div>
    <div class="client"><i></i>Pellant</div>
    <div class="client"><i></i>Nuvari</div>
  </div>
</section>

<section class="touch"><h2>Get in touch</h2></section>

<footer class="site-footer">
  <div class="footer-main">
    <address style="font-style:normal">Quorvan Healthcare Education<br>Level 6, 18 Calder Street<br>Westvale NSW 2090<br>Australia</address>
    <dl>
      <dt>Phone:</dt><dd>+61 2 9000 4172</dd>
      <dt>Facsimile:</dt><dd>+61 2 9000 4173</dd>
      <dt>Email:</dt><dd>info@quorvan.net.au</dd>
    </dl>
    <div class="social"><span></span><span></span><span></span><span></span></div>
  </div>
  <div class="copyright">© 2013 Quorvan Healthcare Education – <b>Privacy Policy</b> – <b>Terms of Service</b></div>
</footer>

<div class="map" role="img" aria-label="Street map showing the office location"></div>

</body>
</html>
```